Superfood Organic Powder needs a new Standup Pouch Design

Superfood brand needs a new package design Standup pouch

We need a new packaging design
*Standup Pouch*
for a NEW superfood product to our brand PureLeafy.

This product is a superfood blend of organic powders such as spiralina, chlorella, wheatgrass etc.

The design should be modern with an organic look, - but feel free to play around with it as you wish.

Our first or *older* product is called Vita Sprouts, and contains superfood powders like Maca, Moringa, Baobab, Spirulina, Chlorella, Wheatgrass

Find measurements for the standup pouch in the attachments.

We can either go with a

a white standup pouch with a slight opacity to it
(see attached sample I have from my supplier)

or

mat white standup pouch

Or Natural Kraft if

The white pouch with a slight opacity to it so you can see the powder through the pouch. One cool thing about this one is that if we have an area in the design with no colors, not even white, that area will be completely transparent, see picture of the sample pouch we have in the attachments.
In the sample photo the spider is completely transparent.

The Mat white pouch is just a basic white standup pouch with a mat finish.
What ever you think is best for your design you can suggest.

In the future we will create multiple products, each product should have its own color style to distinguish between them - this product should use green Color code as one of the green colors used in the logo. Of course not all colors should have that code, but just the identifier for this product. Please present an idea to showcase this identifier, it could be a thick horizontal or vertical line somewhere on the pouch.

The standup pouch will be digitally printed so we can use all areas of the pouch.

Please provide 3D mockup of the design in order to better get an idea of the design.
Remember that I consider you as the expert so I'm very open to any suggestions regarding this design - in the end the main goal is to attract customers and that is your area of expertise.

Please let me know if you have any questions - thanks in advance

I'm looking forward to working with you.

Here are some links I have found that I think is great designs just to give a little insight to my designs wishes.:

https://www.pinboardia.dk/pin/813502794461027315/ https://www.vitalmesa.com/collections/all-superfood-products
https://www.pinboardia.dk/pin/742185093316604827/
https://kreatorhub.dk/product-label-design/contests/print-design-stand-up-resealable-pouch-organic-spice-718230
https://www.pinboardia.dk/pin/630918275541783302/
https://www.pinboardia.dk/pin/27653108894410571/
https://www.pinboardia.dk/pin/806213459930741256/
https://www.pinboardia.dk/pin/952071836614390273/ https://www.pinboardia.dk/pin/384617902155034218/
https://www.pinboardia.dk/pin/73904428830153782/

Reason: Needed more work because I changed manufacturer of standup pouches.

Target Market(s)

Vegans, Organic interested clients, healthy living, Fitness, Juicers

Industry/Entity Type

Health And Wellness

Requirements
Must have
• The following text should be added on front of the label under the product name:
• Danish certified organic
• Superfood blend
• —
• The product contains the following ingredients and should be mentioned on the front - only the ingredients names:
• Maca, Moringa, Baobab, Spirulina, Chlorella, Wheatgrass
• —
• Organic logo:
• Organic EU logo should be present on the back (find logo in the attachments) To the right of the logo the following text is mandatory with Myriad Pro Regular as a type-font: See previous design for instructions.
• "EU-LOGO-HERE"
• DK-ØKO-472
• EU/ikke-EU-jordbrug
• EU/non-EU Agriculture
• Next to the EU organic logo we will place the danish organic logo which is attached as well, you can decide if it should be on the left or right side, it is a red Ø logo ( find in the attachments as well.
• —
• The label should contain a Nutritional Information with the danish language as primary. By law in Denmark the language used should be danish but it is allowed to add the English word after the danish separated by a /
• So it should be titled as Næringsindhold / Nutritional information (Title Bold font)
• And contain the following:
• energi (KJ/kcal)
• • fedt / fat (g)
• • - heraf mættede fedtsyrer / from saturated fat (g)
• • kulhydrat / carbohydrates (g)
• • - heraf sukkerarter / from sugar (g)
• • protein (g)
• • salt (g)
• • kostfibre / dietary fiber (g)
• —
• We need ingredients list on the back as well titled Ingredienser / Ingredients (Title Bold font)
• Maca, Moringa, Baobab, Spirulina, Chlorella, Hvedegræs / Wheatgrass
• Nettovægt / Netto weight 225 gr
• —-
• You can add some cool logos indicating that the product is:
• 100 % organic
• 100% vegan
• No additives
• Non-GMO
• Gluten free
• —
• Instructions (Title Bold font)
• Mix the superfood powder into 250 ml water with a twist of lemon, coconut water, green juice, smoothies, almond milk, or add to your favorit morning meal.
• Serving size 1-2 teaspoon
• Would be great with 3-4 images describing the instructions
• Image 1 could be fruit being put in a blender
• Image 2 could be 1 teaspoon with powder on top of a blender
• Image 3 could be a blender in use
• Image 4 poring the smoothie in to a glass to enjoy
• —
• Opbevaring / Storage (Title Bold font)
• Opbevares tørt og ikke for varmt
• Keep in a cool and dry place away from sunlight
• —
• Batch: (Title Bold font)
• Best before / Bedst før: (Title Bold font)
• —
• Barcode field
• Make room for a barcode
• —
• Produced in EU for: (Title Bold font)
• Lyngkraft IVS
• Tranebærvej 42
• 7321 Gadbjerg Ø
• Denmark
• www.pureleafy.eu (make this bold as well)
• —
• Follow us (Title Bold font)
• Instagram and facebook logo on the back with hashtag #pureleafyeu
• —
• Other than that pureleafy logo can be added as well, it is attached as well.
• I will attach our logo with original AI files.
• —
• Our mission (text)
• We want to provide our customers with the best possible superfood blends. Allowing our customers to get a product packed with antioxidants, vitamins and minerals to elevate their health to the next level. All our products are vegan friendly and GMO free - produced under the best possible circumstances.
• —
Nice to have
• Green color from the logo can be used to get it streamlined.
• Color code c2ce48

```html
<!DOCTYPE html>
<html lang="en">
<head>
<meta charset="utf-8">
<title>Vita Sprouts – Standup Pouch Front</title>
<link href="https://fonts.googleapis.com/css2?family=Jost:wght@500;600;700&family=Questrial&display=swap" rel="stylesheet">
<style>
  :root {
    --stage: #e6e6e6;
    --pouch-light: #fbfbfb;
    --pouch-shade: #e2e2e2;
    --leaf-green: #c2ce48;
    --deep-green: #0f7a45;
    --bright-green: #22b24c;
    --fresh-green: #4fd25a;
    --line-green: #1a9a40;
    --title-grey: #666666;
    --body-grey: #444444;
    --white: #ffffff;
  }
  * { margin: 0; padding: 0; box-sizing: border-box; }
  html, body { width: 1200px; height: 800px; overflow: hidden; }
  body { background: var(--stage); }
  .canvas { position: relative; width: 1200px; height: 800px; overflow: hidden; }

  .pouch {
    position: absolute; left: 410px; top: 70px;
    width: 380px; height: 660px; overflow: hidden;
    background: linear-gradient(90deg, var(--pouch-shade) 0%, var(--pouch-light) 25%, var(--pouch-light) 70%, var(--pouch-shade) 100%);
  }
  .top-band {
    position: absolute; left: 0; top: 0; width: 100%; height: 110px;
    background: linear-gradient(180deg, #27b84a 0%, #5ddc5c 45%, #2cc14f 100%);
  }
  .tear-line {
    position: absolute; left: 0; top: 106px; width: 100%;
    border-top: 2px dashed var(--white);
  }
  .brand {
    position: absolute; left: 78px; top: 150px;
    display: flex; align-items: center; gap: 8px;
  }
  .brand-dot { width: 16px; height: 16px; border-radius: 50%; background: var(--leaf-green); }
  .brand-name {
    font-family: "Jost", sans-serif; font-weight: 500; font-size: 30px;
    color: var(--leaf-green); letter-spacing: 0.5px;
  }
  .product-name { position: absolute; left: 52px; top: 212px; line-height: 1; }
  .product-name .line-1 {
    display: block; font-family: "Jost", sans-serif; font-weight: 700;
    font-size: 84px; color: var(--deep-green); letter-spacing: -1px;
  }
  .product-name .line-2 {
    display: block; margin-top: 2px; font-family: "Questrial", sans-serif;
    font-size: 58px; color: var(--title-grey); letter-spacing: -1px;
  }
  .ingredients {
    position: absolute; left: 60px; top: 385px;
    font-family: "Jost", sans-serif; font-weight: 600; font-size: 20px;
    line-height: 30px; color: var(--deep-green);
  }
  .claim {
    position: absolute; left: 60px; top: 498px;
    font-family: "Questrial", sans-serif; font-size: 15px;
    line-height: 20px; color: var(--body-grey);
  }
  .emblem-area {
    position: absolute; left: 215px; top: 445px; width: 140px; height: 140px;
    border-radius: 50%;
    background: radial-gradient(circle at 50% 50%, var(--fresh-green) 0%, var(--bright-green) 100%);
  }
  .bottom-band { position: absolute; left: 0; bottom: 0; width: 380px; height: 110px; }
  .net-weight {
    position: absolute; left: 38px; bottom: 28px;
    font-family: "Jost", sans-serif; font-weight: 500; font-size: 14px;
    color: var(--white);
  }
</style>
</head>
<body>
<main class="canvas">
  <section class="pouch" aria-label="Vita Sprouts standup pouch front">
    <div class="top-band" role="img" aria-label="Green watercolour texture band across the pouch top"></div>
    <div class="tear-line"></div>

    <div class="brand">
      <span class="brand-dot"></span>
      <span class="brand-name">PureLeafy</span>
    </div>

    <h1 class="product-name">
      <span class="line-1">VITA</span>
      <span class="line-2">SPROUTS</span>
    </h1>

    <p class="ingredients">Maca, Moringa, Baobab<br>Spirulina, Chlorella,<br>Wheatgrass</p>

    <p class="claim">Danish certified<br>organic Superfood<br>blend</p>

    <div class="emblem-area" role="img" aria-label="Green decorative emblem with swirl ornament"></div>

    <svg class="bottom-band" viewBox="0 0 380 110" aria-hidden="true">
      <path d="M0 22 Q190 52 380 8 L380 110 L0 110 Z" fill="var(--bright-green)"/>
      <g fill="none" stroke="var(--line-green)" stroke-width="1.2">
        <path d="M190 60 Q290 48 380 26"/>
        <path d="M200 68 Q295 56 380 36"/>
        <path d="M210 76 Q300 64 380 46"/>
        <path d="M220 84 Q305 72 380 56"/>
        <path d="M230 92 Q310 80 380 66"/>
        <path d="M0 40 Q90 62 180 66"/>
        <path d="M0 50 Q90 72 170 76"/>
      </g>
    </svg>
    <p class="net-weight">Nettovægt / Netto weight 225 gr</p>
  </section>
</main>
</body>
</html>
```